New Zealand Export company needs business cards

We need new business cards to match our new logo for a company based in New Zealand who deal specifically with the Pacific Islands. We source, consolidate and ship products out of New Zealand to the Pacific Islands. Will attach our old ones and also new logo.
Would like the Islands we deal with and the areas of work we have access to, to be included on the business cards.

Contact Information for Business Card

T +64 9 571 3048
F +64 9 571 6285
12-18 Kowhai Lane, Drury, 2113
PO Box 814, Drury, Auckland 2247, New Zealand
www.falconfreight.example.nz
E sales@falconfreight.example.nz

Font styles to use
Sans Serif

Colors
85abd2
33a6d7
ffffff

Requirements
Must have
• A company of PWM

```html
<!DOCTYPE html>
<html lang="en">
<head>
<meta charset="utf-8">
<title>Falcon Freight – Business Card</title>
<link href="https://fonts.googleapis.com/css2?family=Barlow:wght@500;600;700&display=swap" rel="stylesheet">
<style>
  :root {
    --navy: #0d56a6;
    --sky: #33a6d7;
    --stripe: #3dbbe8;
    --mist: #85abd2;
    --ink: #222428;
    --paper: #ffffff;
    --backdrop: #eaf6fc;
  }
  * { margin: 0; padding: 0; box-sizing: border-box; }
  html, body { width: 1200px; height: 1200px; overflow: hidden; }
  body {
    background: var(--backdrop);
    font-family: "Barlow", Arial, sans-serif;
    color: var(--ink);
    position: relative;
  }
  .card {
    position: absolute;
    left: 258px;
    width: 685px;
    height: 391px;
    background: var(--paper);
    overflow: hidden;
    box-shadow: 0 1px 3px rgba(0,0,0,0.18);
  }
  .card--front { top: 180px; }
  .card--back { top: 615px; }

  .stripes { position: absolute; width: 63px; }
  .stripes span {
    display: block;
    height: 7px;
    margin-bottom: 7.4px;
    background: var(--stripe);
  }
  .front-stripes-left { left: 0; top: 42px; }
  .front-stripes-right { right: 0; top: 256px; }
  .back-stripes-right { right: 0; top: 43px; }
  .back-stripes-left { left: 5px; top: 259px; }

  .brand-name {
    position: absolute;
    left: 0; right: 0;
    top: 160px;
    text-align: center;
    font-weight: 700;
    font-size: 40px;
    line-height: 48px;
    letter-spacing: 1px;
    color: var(--navy);
    text-transform: uppercase;
  }
  .brand-rule {
    position: absolute;
    left: 262px;
    width: 160px;
    top: 216px;
    height: 2px;
    background: var(--mist);
  }
  .services {
    position: absolute;
    left: 0; right: 0;
    top: 228px;
    text-align: center;
    font-weight: 600;
    font-size: 13px;
    letter-spacing: 2px;
    text-transform: uppercase;
    color: var(--sky);
  }
  .islands {
    position: absolute;
    left: 80px; right: 80px;
    top: 252px;
    text-align: center;
    font-weight: 500;
    font-size: 13px;
    line-height: 18px;
    color: var(--mist);
  }
  .web {
    position: absolute;
    left: 0; right: 0;
    top: 328px;
    padding-left: 27px;
    text-align: center;
    font-weight: 600;
    font-size: 14px;
    color: var(--ink);
  }

  .person-name {
    position: absolute;
    left: 0; right: 0;
    top: 76px;
    padding-left: 27px;
    text-align: center;
    font-weight: 600;
    font-size: 50px;
    line-height: 1;
    color: var(--navy);
  }
  .person-role {
    position: absolute;
    left: 0; right: 0;
    top: 134px;
    padding-left: 27px;
    text-align: center;
    font-weight: 600;
    font-size: 23px;
    color: var(--ink);
  }

  .contact { position: absolute; display: flex; align-items: flex-start; }
  .contact svg { flex: none; fill: var(--navy); }
  .contact-phone { left: 122px; top: 215px; }
  .contact-fax { left: 121px; top: 265px; }
  .contact-address { left: 320px; top: 210px; }
  .contact-email { left: 319px; top: 268px; }

  .contact-number {
    margin-left: 20px;
    font-weight: 700;
    font-size: 19px;
    letter-spacing: 0.6px;
    line-height: 24px;
  }
  .contact-text {
    margin-left: 20px;
    font-weight: 600;
    font-size: 14.5px;
    line-height: 18px;
  }
  .contact-text .indent { padding-left: 4px; }

  .partner {
    position: absolute;
    left: 0; right: 0;
    top: 328px;
    padding-left: 10px;
    display: flex;
    justify-content: center;
    align-items: center;
    gap: 8px;
  }
  .partner-mark {
    width: 16px; height: 16px;
    background: var(--mist);
  }
  .partner-name {
    font-weight: 700;
    font-size: 24px;
    letter-spacing: 1px;
    color: var(--navy);
  }
</style>
</head>
<body>

<section class="card card--front">
  <div class="stripes front-stripes-left"><span></span><span></span><span></span><span></span><span></span><span></span><span></span></div>
  <div class="brand-name">Falcon Freight</div>
  <div class="brand-rule"></div>
  <div class="services">Sourcing · Consolidation · Shipping</div>
  <div class="islands">Fiji · Samoa · Tonga · Cook Islands · Niue · Vanuatu · Tuvalu · Kiribati</div>
  <div class="web">www.falconfreight.example.nz</div>
  <div class="stripes front-stripes-right"><span></span><span></span><span></span><span></span><span></span><span></span><span></span></div>
</section>

<section class="card card--back">
  <div class="stripes back-stripes-right"><span></span><span></span><span></span><span></span><span></span><span></span><span></span></div>

  <h1 class="person-name">Tessa Hallett</h1>
  <p class="person-role">Sales Manager</p>

  <div class="contact contact-phone">
    <svg width="20" height="20" viewBox="0 0 24 24" aria-hidden="true"><path d="M6.6 10.8c1.4 2.8 3.8 5.1 6.6 6.6l2.2-2.2c.3-.3.7-.4 1-.2 1.1.4 2.3.6 3.6.6.6 0 1 .4 1 1V20c0 .6-.4 1-1 1C10.6 21 3 13.4 3 4c0-.6.4-1 1-1h3.5c.6 0 1 .4 1 1 0 1.3.2 2.5.6 3.6.1.3 0 .7-.2 1L6.6 10.8z"/></svg>
    <span class="contact-number">+64 9 571 3048</span>
  </div>

  <div class="contact contact-fax">
    <svg width="21" height="21" viewBox="0 0 24 24" aria-hidden="true"><path d="M7 2h8l3 3v4H7V2zm-3 8h16a2 2 0 0 1 2 2v6h-4v4H6v-4H2v-6a2 2 0 0 1 2-2zm4 7v3h8v-3H8zm1 1h6v.8H9V18z"/></svg>
    <span class="contact-number">+64 9 571 6285</span>
  </div>

  <div class="contact contact-address">
    <svg width="17" height="20" viewBox="0 0 24 28" aria-hidden="true"><path d="M12 1C6.5 1 2 5.4 2 10.8 2 18 12 27 12 27s10-9 10-16.2C22 5.4 17.5 1 12 1zm0 14a4 4 0 1 1 0-8 4 4 0 0 1 0 8z"/></svg>
    <div class="contact-text">
      12-18 Kowhai Lane, Drury, 2113<br>
      PO Box 814, Drury, Auckland 2247,<br>
      <span class="indent">New Zealand</span>
    </div>
  </div>

  <div class="contact contact-email">
    <svg width="20" height="16" viewBox="0 0 24 18" aria-hidden="true"><path d="M1 1h22v16H1V1zm2 2.2V15h18V3.2l-9 7-9-7zM4.6 3 12 8.7 19.4 3H4.6z"/></svg>
    <span class="contact-text">sales@falconfreight.example.nz</span>
  </div>

  <div class="partner">
    <span class="partner-mark"></span>
    <span class="partner-name">PWM</span>
  </div>

  <div class="stripes back-stripes-left"><span></span><span></span><span></span><span></span><span></span><span></span><span></span></div>
</section>

</body>
</html>
```